Business card design for Plumbing and Gas fitting company

We need a business card design for our plumbing and gas fitting company using the company logo and director details. Design should be modern and eye-catching however kept reasonably simple. This design should be targeted at commercial businesses/work so professionalism is key.

Target Market(s)

Commercial/business

Industry/Entity Type

Plumbing

Contact Information for Business Card

Warren Dohey
Director
027 581 9043
warren@vantorplumbingandgas.example
PO Box 7816
Palmerston North 4472

Font styles to use
Sans Serif

Requirements
Must have
• Logo
• Modern
• Kept simple
Nice to have
• Colour scheme based around logo

```html
<!DOCTYPE html>
<html lang="en">
<head>
<meta charset="utf-8">
<title>Vantor Plumbing &amp; Gas – Business Card</title>
<link rel="stylesheet" href="https://fonts.googleapis.com/css2?family=Source+Sans+3:wght@400;600;700&display=swap">
<style>
  :root {
    --backdrop: #2a2a2c;
    --card: #1b1b1d;
    --brand-blue: #1c7fd8;
    --brand-orange: #e8782a;
    --text-light: #e6e6e6;
    --text-muted: #a8a8a8;
  }
  * { margin: 0; padding: 0; box-sizing: border-box; }
  html, body {
    width: 1200px;
    height: 900px;
    overflow: hidden;
    background: var(--backdrop);
    font-family: "Source Sans 3", sans-serif;
  }
  .stage {
    position: relative;
    width: 1200px;
    height: 900px;
  }
  .card {
    position: absolute;
    top: 300px;
    width: 525px;
    height: 300px;
    background: var(--card);
    border-radius: 18px;
    overflow: hidden;
  }
  .card--front { left: 50px; }
  .card--back { left: 625px; }

  .brand {
    display: flex;
    align-items: center;
    gap: 10px;
    color: var(--brand-blue);
    font-weight: 700;
    white-space: nowrap;
  }
  .brand__dot {
    width: 14px;
    height: 14px;
    border-radius: 50%;
    background: var(--brand-orange);
  }
  .card--front .brand {
    position: absolute;
    left: 34px;
    top: 34px;
    font-size: 26px;
  }
  .rule {
    position: absolute;
    height: 1.5px;
    background: var(--brand-orange);
  }
  .rule--top { left: 330px; right: 0; top: 52px; }
  .rule--bottom { left: 0; right: 0; top: 228px; }

  .contact {
    position: absolute;
    left: 0;
    right: 0;
    top: 92px;
    text-align: center;
    color: var(--text-light);
    font-size: 15px;
    line-height: 1.35;
  }
  .contact__name {
    font-size: 23px;
    font-weight: 400;
    letter-spacing: 0.5px;
    line-height: 1.1;
  }
  .contact__first { color: var(--brand-blue); }
  .contact__last { color: var(--brand-orange); }
  .contact__role {
    font-size: 13px;
    color: var(--text-muted);
    margin-bottom: 8px;
  }
  .contact__label { color: var(--brand-orange); font-weight: 600; }

  .address {
    position: absolute;
    left: 0;
    right: 0;
    top: 246px;
    text-align: center;
    color: var(--text-light);
    font-size: 16px;
  }

  .card--back .brand {
    position: absolute;
    inset: 0;
    justify-content: center;
    font-size: 32px;
  }
  .card--back .brand__dot { width: 18px; height: 18px; }
</style>
</head>
<body>
<main class="stage">
  <section class="card card--front" aria-label="Business card front">
    <div class="brand">
      <span class="brand__name">Vantor Plumbing &amp; Gas</span>
      <span class="brand__dot"></span>
    </div>
    <div class="rule rule--top"></div>
    <div class="contact">
      <p class="contact__name"><span class="contact__first">WARREN</span> <span class="contact__last">DOHEY</span></p>
      <p class="contact__role">Director</p>
      <p><span class="contact__label">P:</span> 027 581 9043</p>
      <p><span class="contact__label">E:</span> warren@vantorplumbingandgas.example</p>
    </div>
    <div class="rule rule--bottom"></div>
    <p class="address">PO Box 7816 Palmerston North 4472</p>
  </section>

  <section class="card card--back" aria-label="Business card back">
    <div class="brand">
      <span class="brand__name">Vantor Plumbing &amp; Gas</span>
      <span class="brand__dot"></span>
    </div>
  </section>
</main>
</body>
</html>
```